brisk pelts buisness card design

I need a buisness card that has an orange and red outline a side on antelopes head with long horns.I love the one I found on searchly but it has a watermark see below,would it be possible to have something similar?
There is only one other supplier of skins on the sunshine coast ,very expensive and there are a lot of Australian hides.I can supply
a less expensive choice which is extremly different.

Target Market(s)

home owners family stylists bulk buying anniverary wedding gifts

Industry/Entity Type

Searchly

Contact Information for Business Card

BRISK PELTS
EXOTIC HOMEWARES FOR THE MODERN HOME
MIRANDA 0417263948 bellamoor@examplemail.test
imported from Africa no single product the same

Requirements
Must have
• on front BRISK PELTS large either side of logo
red and orange

ethically produced
Nice to have
• I still have to have more pics of gear set up so just one on back
Should not have
• live animals research shows people dont like to look at animal
no running writing

```html
<!DOCTYPE html>
<html lang="en">
<head>
<meta charset="utf-8">
<title>Brisk Pelts – Business Card</title>
<link rel="stylesheet" href="https://fonts.googleapis.com/css2?family=Advent+Pro:wght@200;300&family=Oswald:wght@400&family=Pathway+Gothic+One&display=swap">
<style>
  :root {
    --red: #e8262a;
    --orange: #f5871f;
    --ink: #111111;
    --black: #000000;
    --grey-light: #f4f4f5;
    --grey-mid: #c9cacc;
  }
  html, body {
    margin: 0;
    padding: 0;
    width: 968px;
    height: 1200px;
    overflow: hidden;
    background: #ffffff;
  }
  .canvas {
    position: relative;
    width: 968px;
    height: 1200px;
    overflow: hidden;
  }
  .card {
    position: absolute;
    left: 0;
    width: 968px;
    overflow: hidden;
    background: radial-gradient(ellipse 60% 70% at 50% 55%, var(--grey-light) 0%, #e2e3e4 55%, var(--grey-mid) 100%);
  }
  .card--front { top: 0; height: 602px; }
  .card--back { top: 602px; height: 598px; }

  .wordmark {
    position: absolute;
    margin: 0;
    font-family: "Advent Pro", sans-serif;
    font-weight: 200;
    font-size: 100px;
    line-height: 1;
    white-space: nowrap;
    color: var(--ink);
    letter-spacing: 1px;
  }
  .wordmark .accent { color: var(--red); }
  .card--front .wordmark {
    top: 56px;
    left: 0;
    width: 968px;
    text-align: center;
  }
  .card--back .wordmark {
    top: 26px;
    right: 38px;
  }

  .side-tab {
    position: absolute;
    top: 213px;
    width: 43px;
    height: 134px;
    background: var(--orange);
  }
  .side-tab--left { left: 0; border-radius: 0 24px 24px 0; }
  .side-tab--right { right: 0; width: 51px; border-radius: 24px 0 0 24px; }

  .brand-mark {
    position: absolute;
    display: flex;
    flex-direction: column;
    align-items: center;
    justify-content: center;
    gap: 14px;
    font-family: "Advent Pro", sans-serif;
    font-weight: 300;
    font-size: 24px;
    letter-spacing: 2px;
    color: var(--orange);
    white-space: nowrap;
  }
  .brand-mark .dot {
    width: 22px;
    height: 22px;
    border-radius: 50%;
    background: var(--red);
  }
  .card--front .brand-mark { left: 404px; top: 190px; width: 170px; height: 283px; }
  .card--back .brand-mark { left: 66px; top: 162px; width: 170px; height: 279px; }

  .tagline-band {
    position: absolute;
    left: 0;
    top: 489px;
    width: 968px;
    height: 113px;
    background: var(--black);
    display: flex;
    align-items: center;
    justify-content: center;
  }
  .tagline {
    margin: 0;
    font-family: "Oswald", sans-serif;
    font-weight: 400;
    font-size: 42px;
    line-height: 1;
    letter-spacing: 0.5px;
    color: var(--orange);
    white-space: nowrap;
  }
  .tagline .initial { color: var(--red); }

  .pennant {
    position: absolute;
    left: 0;
    top: 0;
  }

  .contact {
    margin: 0;
    font-family: "Pathway Gothic One", sans-serif;
    font-style: normal;
    color: var(--ink);
  }
  .contact__phone {
    position: absolute;
    right: 40px;
    top: 156px;
    display: flex;
    align-items: center;
    gap: 10px;
    font-size: 26px;
    line-height: 1;
    white-space: nowrap;
  }
  .contact__email {
    position: absolute;
    right: 40px;
    top: 202px;
    font-size: 36px;
    line-height: 1;
    white-space: nowrap;
  }
  .promise {
    position: absolute;
    right: 38px;
    top: 508px;
    margin: 0;
    font-family: "Pathway Gothic One", sans-serif;
    font-size: 48px;
    line-height: 1;
    color: var(--ink);
    white-space: nowrap;
  }
</style>
</head>
<body>
<main class="canvas">

  <section class="card card--front" aria-label="Card front">
    <div class="side-tab side-tab--left"></div>
    <div class="side-tab side-tab--right"></div>

    <h1 class="wordmark"><span class="accent">B</span>RIS<span class="accent">K</span> <span class="accent">P</span>ELT<span class="accent">S</span></h1>

    <div class="brand-mark" role="img" aria-label="Brisk Pelts brand mark">
      <span class="dot"></span>
      <span>BRISK PELTS</span>
    </div>

    <div class="tagline-band">
      <p class="tagline"><span class="initial">E</span>XOTIC <span class="initial">H</span>OMEWARES <span class="initial">F</span>OR THE <span class="initial">M</span>ODERN <span class="initial">H</span>OME <span class="initial">M</span>IRANDA</p>
    </div>
  </section>

  <section class="card card--back" aria-label="Card back">
    <svg class="pennant" width="540" height="598" viewBox="0 0 540 598" aria-hidden="true">
      <polygon points="0,0 527,299 0,598" fill="var(--orange)"/>
      <polygon points="0,15 501,299 0,583" fill="var(--black)"/>
    </svg>

    <div class="brand-mark" role="img" aria-label="Brisk Pelts brand mark">
      <span class="dot"></span>
      <span>BRISK PELTS</span>
    </div>

    <h2 class="wordmark"><span class="accent">B</span>RIS<span class="accent">K</span> <span class="accent">P</span>ELT<span class="accent">S</span></h2>

    <address class="contact">
      <span class="contact__phone">
        <svg width="44" height="24" viewBox="0 0 44 26" aria-hidden="true">
          <path d="M2 9 C2 2 42 2 42 9 L42 12 L32 12 L32 8 C26 6 18 6 12 8 L12 12 L2 12 Z" fill="var(--ink)"/>
          <path d="M11 14 L33 14 L38 25 L6 25 Z" fill="var(--ink)"/>
          <circle cx="22" cy="19" r="3.5" fill="var(--grey-light)"/>
        </svg>
        0417263948
      </span>
      <span class="contact__email">bellamoor@examplemail.test</span>
    </address>

    <p class="promise">Imported From Africa No Single Product The Same</p>
  </section>

</main>
</body>
</html>
```